Logo and website for K-12 Academy- Lumora Pathis Academy

Overview
Lumora Pathis Academy is a new online educational institution based in Ghana & Portugal, offering a K-12 curriculum designed to empower the next generation with academic excellence, leadership skills, and deep-rooted cultural values. The academy emphasizes knowledge, mentorship, leadership, and a strong connection to African heritage.

Objective
Create a meaningful, timeless, and visually compelling logo that:

Represents growth, wisdom, and resilience through the imagery of the Odum Tree.

Symbolizes knowledge and academic pursuit.

Reflects mentorship and leadership development.

Appeals to parents and students alike, exuding trust, strength, and inspiration.

Key Themes
Odum Tree: A powerful symbol in Ghana, representing strength, endurance, and wisdom.

Knowledge: Books, light, open pathways, or abstract symbols of learning.

Mentorship/Leadership: Hands guiding others, rising figures, light leading the way, or interconnected branches.

Ghanaian Heritage: Subtle inclusion of Ghanaian cultural elements (such as color palette or patterns) without overwhelming the global, professional appeal.

Target Audience
Parents and guardians seeking quality education steeped in both academic rigor and cultural values.
Students from kindergarten through high school (ages 4–18).
Stakeholders and partners supporting education initiatives in Africa.

Style & Tone
Professional and Inspirational: Serious but welcoming.
Modern with Cultural Depth: Clean lines, minimal clutter, but with depth and meaning.
Warm and Trustworthy: The logo should evoke feelings of safety, hope, growth, and pride.
Flexible: It should work well in both full-color and monochrome versions, and look good at both large and small scales. Except for color changes and cultural elements, main logo should be able to be adapted to both countries
Color Palette (Suggestions)
Earth tones: Browns, greens — representing the Odum tree and growth
Gold/Yellow: For wisdom, enlightenment, and a nod to Ghana’s national colors.
Deep Red or Burgundy: Representing strength and heritage.
Logo Elements
Tree: Odum tree as the main, central symbol. Book, Light, or Path: Sub-elements to subtly symbolize knowledge and learning.
Mentorship: Perhaps visualized through multiple branches, a larger tree protecting smaller saplings, or guiding light themes.

Deliverables
Primary logo (full-color)
Secondary logo (single-color or black/white version)
Icon or emblem version (simplified for small applications like favicons or social media)
Logo usage guidelines (optional but preferred)

Target Market(s)

K-12 parents

Industry/Entity Type

Education

Coding

Coded - Design and coding required

Number of Pages Required

1 page

Font styles to use
Sans Serif

Requirements
Nice to have
• Inspirations Cultural motifs reimagined in a sleek, contemporary style. Nature-inspired logos that convey growth and resilience.

```html
<!DOCTYPE html>
<html lang="en">
<head>
<meta charset="utf-8">
<title>Lumora Pathis Academy</title>
<link href="https://fonts.googleapis.com/css2?family=Jost:wght@400;500;600;700&family=Poppins:wght@400;500;600&display=swap" rel="stylesheet">
<style>
:root{
  --ink:#161616;
  --dark:#121212;
  --yellow:#f2b21c;
  --green:#2f6b2c;
  --green-deep:#245722;
  --red:#b42a22;
  --text:#555;
  --muted:#8a8a8a;
  --white:#ffffff;
  --line:#e6e6e6;
}
*{box-sizing:border-box;margin:0;padding:0}
html,body{width:1200px;height:3724px;overflow:hidden;background:var(--white)}
body{font-family:"Poppins",sans-serif;color:var(--text);position:relative}
h1,h2,h3,h4{font-family:"Jost",sans-serif;color:var(--ink)}
.abs{position:absolute}

/* hero */
.hero{position:absolute;left:0;top:0;width:1200px;height:560px;background:var(--dark);overflow:hidden}
.hero-photo{position:absolute;right:0;top:0;width:720px;height:560px;background:linear-gradient(90deg,var(--dark) 0%,#2a2219 22%,#5a4026 55%,#7a5a34 80%,#3c2d1e 100%)}
.nav{position:absolute;left:0;top:0;width:1200px;height:70px;display:flex;align-items:center;padding:0 60px}
.brand{display:flex;align-items:center;gap:10px;font-family:"Jost",sans-serif;font-weight:600;font-size:16px;color:var(--white)}
.brand-dot{width:36px;height:36px;border-radius:50%;background:var(--yellow)}
.menu{margin-left:auto;display:flex;gap:34px;list-style:none;font-size:14px;color:var(--white);margin-right:60px}
.menu li.active{color:var(--yellow);border-bottom:2px solid var(--yellow);padding-bottom:4px}
.search{position:absolute;left:445px;top:50px}
.hero-copy{position:absolute;left:60px;top:160px;width:440px;color:var(--white)}
.hero-copy h1{color:var(--white);font-size:50px;font-weight:600;line-height:1.05}
.hero-copy .tag{font-family:"Jost",sans-serif;font-size:20px;font-weight:500;margin-top:10px}
.ticks{list-style:none;margin-top:16px;font-size:14px}
.ticks li{display:flex;align-items:center;gap:12px;margin-bottom:9px}
.btns{display:flex;gap:16px;margin-top:22px}
.btn{display:inline-block;padding:12px 22px;border-radius:6px;font-size:14px;font-weight:500}
.btn-yellow{background:var(--yellow);color:var(--ink)}
.btn-green{background:var(--green);color:var(--white)}
.hero-wave{position:absolute;left:0;top:500px}

/* about */
.about-photo{left:80px;top:600px;width:420px;height:420px;border-radius:50%;background:radial-gradient(circle at 40% 40%,#6b7a8a,#2d3a44 70%);border:8px solid #f3f3f3}
.about-inset{left:380px;top:860px;width:180px;height:180px;border-radius:50%;background:radial-gradient(circle,#8a6a4a,#4a3526);border:6px solid var(--white)}
.about-copy{left:660px;top:730px;width:470px}
.about-copy h2{font-size:44px;font-weight:600;margin-bottom:14px}
.about-copy p{font-size:13px;line-height:1.75;margin-bottom:14px}

/* tree values */
.tree-art{left:370px;top:1280px;width:460px;height:480px;border-radius:50% 50% 8px 8px;background:radial-gradient(ellipse at 50% 35%,#d6a22a 0%,#a8461f 35%,#3f6b2c 60%,#2a2a2a 85%,transparent 86%)}
.value{position:absolute;width:210px;font-size:13px;line-height:1.5;color:var(--ink)}
.value.left{text-align:right}
.badge{position:absolute;width:44px;height:44px;border-radius:50%;display:flex;align-items:center;justify-content:center}
.badge.red{background:var(--red)}
.badge.green{background:var(--green)}

/* offer */
.offer{position:absolute;left:0;top:1760px;width:1200px;height:660px;background:var(--dark)}
.offer h2{color:var(--white);text-align:center;font-size:42px;font-weight:600;margin-top:70px}
.offer .sub{color:#cfcfcf;text-align:center;font-size:14px;margin-top:4px}
.cards{display:flex;gap:30px;justify-content:center;margin-top:30px}
.card{width:300px;background:var(--white);border-radius:10px;overflow:hidden;text-align:center;position:relative;padding-bottom:22px}
.card-img{height:190px}
.card-icon{width:50px;height:50px;border-radius:50%;margin:-25px auto 0;border:4px solid var(--white);position:relative}
.card h3{font-size:15px;font-weight:600;margin:10px 0 8px;letter-spacing:.3px}
.card p{font-size:12px;line-height:1.6;padding:0 24px}

/* testimonials */
.reviews{position:absolute;left:0;top:2470px;width:1200px}
.reviews h2{text-align:center;font-size:40px;font-weight:600}
.reviews .sub{text-align:center;font-size:14px;margin-top:4px}
.quotes{display:flex;gap:40px;justify-content:center;margin-top:40px}
.quote{width:480px;height:230px;background:var(--white);border-radius:12px;box-shadow:0 6px 24px rgba(0,0,0,.1);padding:44px 40px 0;text-align:center;position:relative}
.quote p{font-size:13px;line-height:1.7}
.qmark{position:absolute;top:-18px;font-family:"Jost",sans-serif;font-size:70px;color:#444;line-height:1}
.qmark.l{left:20px}.qmark.r{right:20px}
.author{display:flex;justify-content:center;align-items:center;gap:14px;margin-top:20px}
.author h4{font-size:14px;color:var(--green);text-align:right}
.author span{font-size:11px;color:var(--muted)}
.avatar{width:44px;height:44px;border-radius:50%;background:linear-gradient(135deg,#9a8a7a,#4a4038)}
.arrows{position:absolute;left:1125px;top:165px}
.arrow{width:24px;height:24px;border-radius:50%;background:#444;margin-bottom:16px;display:flex;align-items:center;justify-content:center}

/* cta */
.cta-tree{left:320px;top:3000px;width:560px;height:330px;border-radius:50% 50% 0 0;background:radial-gradient(ellipse at 50% 40%,#eeeeee,#f7f7f7 60%,transparent 70%)}
.cta{position:absolute;left:0;top:2960px;width:1200px;text-align:center}
.cta h2{font-size:36px;font-weight:600;line-height:1.25}
.cta p{font-size:13px;line-height:1.6;width:560px;margin:16px auto 0}
.signup{width:580px;height:48px;margin:28px auto 0;border-radius:26px;background:var(--white);box-shadow:0 4px 16px rgba(0,0,0,.12);display:flex;align-items:center;padding:0 4px 0 16px;gap:10px;font-size:12px;color:var(--muted)}
.signup .go{margin-left:auto;background:var(--yellow);color:var(--ink);border-radius:22px;padding:11px 34px;font-size:13px;font-weight:500}

/* footer */
.footer{position:absolute;left:0;top:3260px;width:1200px;height:464px;background:var(--green);color:var(--white);text-align:center}
.footer-curve{position:absolute;left:0;top:-1px}
.footer-brand{position:absolute;left:510px;top:-10px;width:180px;height:180px;border-radius:50%;background:var(--white);border:6px solid var(--yellow);display:flex;align-items:center;justify-content:center;font-family:"Jost",sans-serif;font-weight:600;font-size:17px;color:var(--ink);padding:20px;line-height:1.2}
.contact{position:absolute;top:100px;width:260px;text-align:center;font-size:14px}
.contact .ic{width:60px;height:60px;border-radius:50%;background:var(--yellow);margin:0 auto 14px;display:flex;align-items:center;justify-content:center}
.footer-nav{position:absolute;left:0;top:288px;width:1200px;display:flex;justify-content:center;gap:46px;list-style:none;font-size:14px}
.socials{position:absolute;left:0;top:332px;width:1200px;display:flex;justify-content:center;gap:12px}
.socials span{width:28px;height:28px;border-radius:50%;background:var(--yellow)}
.copy{position:absolute;left:0;top:382px;width:1200px;font-size:12px}
</style>
</head>
<body>

<header class="hero">
  <div class="hero-photo" role="img" aria-label="Photo of smiling graduates in caps and gowns"></div>
  <nav class="nav">
    <div class="brand"><span class="brand-dot"></span>Lumora Pathis Academy</div>
    <ul class="menu">
      <li class="active">Home</li><li>About Us</li><li>What We Offer</li><li>Reviews</li><li>Blogs</li><li>Get In Touch</li>
    </ul>
  </nav>
  <svg class="search" width="14" height="14" viewBox="0 0 14 14"><circle cx="6" cy="6" r="4.5" fill="none" stroke="#fff" stroke-width="1.6"/><line x1="9.5" y1="9.5" x2="13" y2="13" stroke="#fff" stroke-width="1.6"/></svg>
  <div class="hero-copy">
    <h1>Educating<br>Africa's Future</h1>
    <div class="tag">Rooted in Heritage, Built for Excellence</div>
    <ul class="ticks">
      <li><svg width="14" height="14" viewBox="0 0 14 14"><path d="M2 7l3 3 7-7" fill="none" stroke="#f2b21c" stroke-width="2"/></svg>Personalized online learning</li>
      <li><svg width="14" height="14" viewBox="0 0 14 14"><path d="M2 7l3 3 7-7" fill="none" stroke="#f2b21c" stroke-width="2"/></svg>Mentorship &amp; student support</li>
      <li><svg width="14" height="14" viewBox="0 0 14 14"><path d="M2 7l3 3 7-7" fill="none" stroke="#f2b21c" stroke-width="2"/></svg>Integration of African cultural education</li>
      <li><svg width="14" height="14" viewBox="0 0 14 14"><path d="M2 7l3 3 7-7" fill="none" stroke="#f2b21c" stroke-width="2"/></svg>Leadership development programs</li>
    </ul>
    <div class="btns"><span class="btn btn-yellow">Enroll Now</span><span class="btn btn-green">Book a Virtual Tour</span></div>
  </div>
  <svg class="hero-wave" width="1200" height="60" viewBox="0 0 1200 60"><path d="M0 34 C200 10 400 50 600 30 S1000 8 1200 28 V60 H0Z" fill="#fff"/><path d="M0 34 C200 10 400 50 600 30 S1000 8 1200 28" fill="none" stroke="#f2b21c" stroke-width="6"/></svg>
</header>

<section class="about">
  <div class="abs about-photo" role="img" aria-label="Photo of children learning on a laptop"></div>
  <div class="abs about-inset" role="img" aria-label="Photo of a student holding a globe"></div>
  <div class="abs about-copy">
    <h2>About Us</h2>
    <p>We are an online K-12 school that blends strong academics with African heritage. Our teachers guide every learner with care, clear goals and steady support, so each child can grow in confidence, curiosity and skill from the first lesson onward.</p>
    <p>Students join live classes, work with mentors and build leadership habits that last. Families stay close to progress through regular updates, and our community connects learners across Ghana, Portugal and beyond in one shared classroom.</p>
    <span class="btn btn-green">Book a Virtual Tour</span>
  </div>
</section>

<section class="values">
  <div class="abs tree-art" role="img" aria-label="Illustration of a large Odum tree growing from an open book"></div>
  <div class="badge red" style="left:410px;top:1280px"></div>
  <div class="value left" style="left:180px;top:1280px">K-12 curriculum designed to Leadership skills</div>
  <div class="badge green" style="left:300px;top:1400px"></div>
  <div class="value left" style="left:70px;top:1400px">Empower the next generation with academic excellence</div>
  <div class="badge green" style="left:250px;top:1590px"></div>
  <div class="value left" style="left:20px;top:1590px">Online educational institution based in Ghana</div>
  <div class="badge red" style="left:740px;top:1280px"></div>
  <div class="value" style="left:800px;top:1285px">Deep-rooted cultural values</div>
  <div class="badge green" style="left:880px;top:1400px"></div>
  <div class="value" style="left:940px;top:1400px">The academy emphasizes knowledge, mentorship</div>
  <div class="badge red" style="left:880px;top:1590px"></div>
  <div class="value" style="left:940px;top:1595px">A strong connection to African heritage</div>
</section>

<section class="offer">
  <h2>What We Offer</h2>
  <div class="sub">Clear learning paths for every stage of a child's growth</div>
  <div class="cards">
    <article class="card">
      <div class="card-img" role="img" aria-label="Photo of young pupils in a classroom" style="background:linear-gradient(135deg,#3a6ea5,#c9a24a)"></div>
      <div class="card-icon" style="background:var(--green)"></div>
      <h3>PRIMARY (FOUNDATIONS)</h3>
      <p>Early reading, numbers and culture taught through play, stories and friendly guided lessons.</p>
    </article>
    <article class="card">
      <div class="card-img" role="img" aria-label="Photo of graduates celebrating" style="background:linear-gradient(135deg,#2a2a2a,#8a6a3a)"></div>
      <div class="card-icon" style="background:var(--yellow)"></div>
      <h3>EXPLORATION &amp; GROWTH</h3>
      <p>Middle years that build deeper subject skills, teamwork and confident independent study.</p>
    </article>
    <article class="card">
      <div class="card-img" role="img" aria-label="Photo of students in a leadership workshop" style="background:linear-gradient(135deg,#6a5a4a,#cfc4b4)"></div>
      <div class="card-icon" style="background:var(--red)"></div>
      <h3>LEADERSHIP &amp; SPECIALIZATION</h3>
      <p>High school tracks with mentors, leadership projects and focused university preparation.</p>
    </article>
  </div>
</section>

<section class="reviews">
  <h2>Parent &amp; Student Testimonials</h2>
  <div class="sub">Kind words from the families who learn with us</div>
  <div class="quotes">
    <div class="quote">
      <span class="qmark l">&ldquo;</span><span class="qmark r">&rdquo;</span>
      <p>Our son now looks forward to every class. His teachers know him well, his mentor checks in each week, and he talks proudly at dinner about the history and culture he is learning online.</p>
      <div class="author"><div><h4>Daniel Okoro</h4><span>Alex Father, Africa</span></div><div class="avatar" role="img" aria-label="Parent portrait"></div></div>
    </div>
    <div class="quote">
      <span class="qmark l">&ldquo;</span><span class="qmark r">&rdquo;</span>
      <p>The lessons are clear, the pace fits my daughter, and the leadership projects have made her braver. We feel part of a real school community even though we study from home.</p>
      <div class="author"><div><h4>Daniel Okoro</h4><span>Alex Father, Africa</span></div><div class="avatar" role="img" aria-label="Parent portrait"></div></div>
    </div>
  </div>
  <div class="arrows">
    <div class="arrow"><svg width="8" height="8" viewBox="0 0 8 8"><path d="M5 1L2 4l3 3" fill="none" stroke="#fff" stroke-width="1.5"/></svg></div>
    <div class="arrow"><svg width="8" height="8" viewBox="0 0 8 8"><path d="M3 1l3 3-3 3" fill="none" stroke="#fff" stroke-width="1.5"/></svg></div>
  </div>
</section>

<div class="abs cta-tree" role="img" aria-label="Faint tree decoration"></div>
<section class="cta">
  <h2>Be Part of the Movement to Redefine<br>African Education</h2>
  <p>Join our mailing list for open days, enrollment dates and news from our growing community of learners, mentors and families.</p>
  <div class="signup">
    <svg width="14" height="12" viewBox="0 0 14 12"><rect x="1" y="1" width="12" height="10" fill="none" stroke="#999" stroke-width="1.3"/><path d="M1 1l6 5 6-5" fill="none" stroke="#999" stroke-width="1.3"/></svg>
    Enter Your Email Address
    <span class="go">Sign Up Here</span>
  </div>
</section>

<footer class="footer">
  <svg class="footer-curve" width="1200" height="60" viewBox="0 0 1200 60"><path d="M0 0 H1200 V20 C900 60 300 60 0 20Z" fill="#fff"/></svg>
  <div class="footer-brand">Lumora Pathis Academy</div>
  <div class="contact" style="left:130px">
    <div class="ic"><svg width="24" height="18" viewBox="0 0 24 18"><rect x="1" y="1" width="22" height="16" rx="2" fill="none" stroke="#fff" stroke-width="2"/><path d="M1 2l11 8 11-8" fill="none" stroke="#fff" stroke-width="2"/></svg></div>
    Email Address:<br>info@lumorapathisacademy.com
  </div>
  <div class="contact" style="left:810px">
    <div class="ic"><svg width="22" height="22" viewBox="0 0 24 24"><path d="M6 2l4 5-2 3c1 3 3 5 6 6l3-2 5 4-3 4C10 22 2 14 2 5z" fill="#fff"/></svg></div>
    Call Us:<br>+1 555 014 2286
  </div>
  <ul class="footer-nav"><li>Home</li><li>About Us</li><li>What We Offer</li><li>Reviews</li><li>Blogs</li><li>Get In Touch</li></ul>
  <div class="socials"><span></span><span></span><span></span><span></span></div>
  <div class="copy">(C) Copyright | All Rights Reserved</div>
</footer>

</body>
</html>
```